Mockup design for a fashion contest website

The website is a landing page for a fashion contest. Participants are fashion students, designers, merchandisers, stylists, and other fashion enthusiasts. Website should have a clean, modern look and should be "headline-y" in nature. Website should be very visual with good use of images since the audience is fashion (specifically women's clothing). Contestants will earn points by identifying fashion/clothing items within images.

Here's what I am thinking:

Title:
Fashion Contest by Vendrow

Headlines (each with subheadline of 10-15 words )
Can you find the features in the image?
This will be a carousel showing 3-4 images with callouts
Have callouts for each of the categories like this: https://img.qorvexa.example/v/7TmWq2LpZr/fullview.jpg
Broad categories for items are labeled like:
Top
Dress
Jeans
Pants
Shorts
Blouse
Skirt
Standard
Crop Top
Shirt
Sweater
Detail fashion attributes are in the spreadsheet attached

Earn Points
and see where you stand -- leaderboard graphic
Win Prizes
Need a way to show multiple prizes here:
Grand prizes: Tablo Max, Kelvar Snapline KZ-TR720Q Wi-Fi Digital Camera, Halden QM480TXV Sewing Machine, Drevo Linemark Plus Drawing tablet
Other prizes: Noral Earlets, Gift cards to great stores: Vimo, Keto, Lumirel, etc.

What You Need To Know
How to Enter (25-30 words)
How do I qualify? (10-15 words)
What are the contest dates (10-15 words)
What is this for? (10-15 words)

----

Tell Your Friends (10 words) [Needs to be shown more prominently as we will have referral bonuses]

The Legal Stuff / Terms & Conditions
[Each subsection 50 words]
Eligibility
Winners & Prizes
Privacy Policy
Judging
Disclaimer

Other sections (shown as links on top perhaps)
Blog - standard blog format. No need for design
Forum - use threadhall software. No need for design
Standings
FAQ
Contact - link to email - no need for design

Need to have clear CTA to sign up on bottom.

Need to Design ‘Standings’ Page:

Show Leaderboard
Ranking, Username, total points, change in ranking (up or down)

Show Total number of images processed. This can be progress bar like in crowdfunding sites:
https://snapdrop.example/kWtrb/91ab3d6f27.png
It would say:
300,000 images processed by 1,000 participants
x% of 1,000,000 goal a month left

Goals and Stretch Goals for the Contest

500,000 images
Grand prizes (1 winner)
Other prizes (3 winners)

1,000,000 images
Grand prizes (2 winners)
Other prizes (6 winners)

2,000,000 images
Grand prizes (3 winners)
Other prizes (9 winners)

3,000,000 images
Grand prizes (4 winners)
Other prizes (12 winners)

How to Earn Points

Points awarded for correctly completing task
Points are deducted for making mistakes and unnecessary skips

Help
just a click away. Post a message on the community forum and ask a question.
----
High contrasty (black & white) with one color perhaps blue should be color palette. Look at our logo for design motif ideas.

Welcome to the contest. I will be guaranteeing the project once at least one usable design comes in. Good luck to all! Added Tuesday, March 14, 2017

Target Market(s)

Fashion community

Industry/Entity Type

Fashion

Number of Pages Required

2 page

Font styles to use
Sans Serif

Requirements
Must have
• one page scroll website (the quiz is a separate page though)
• beautiful graphics and images
• placeholder text where number of words is written
Nice to have
• written copy ideas
Should not have
• the vendrow logo should not be prominently featured. the emphasis is on 'Fashion Contest'

```html
<!DOCTYPE html>
<html lang="en">
<head>
<meta charset="utf-8">
<title>Fashion Contest by Vendrow</title>
<link rel="stylesheet" href="https://fonts.googleapis.com/css2?family=Oswald:wght@300;400;500;600&family=Roboto:wght@300;400;500;700&display=swap">
<style>
:root{
  --blue:#3b93da;
  --ink:#222;
  --footer:#262626;
  --text:#8a8a8a;
  --line:#e4e4e4;
  --white:#fff;
  --table-head:#474747;
  --score-neg:#5b5b5b;
}
*{margin:0;padding:0;box-sizing:border-box}
html,body{width:1200px;height:4082px;overflow:hidden}
body{font-family:"Roboto",Arial,sans-serif;color:var(--ink);background:var(--white);font-size:13px}
section,header,footer{overflow:hidden}
.wrap{width:1026px;margin:0 auto;position:relative}
p{line-height:1.75;color:var(--text);font-size:12.5px}

/* nav */
.topbar{height:82px;display:flex;align-items:center;justify-content:space-between;padding:0 87px}
.brand{display:flex;align-items:center;gap:10px;font-family:"Oswald",sans-serif;font-weight:400;font-size:25px;letter-spacing:1px;color:var(--ink)}
.brand-mark{width:18px;height:18px;background:var(--ink)}
.menu{display:flex;align-items:center;font-size:12px;font-weight:500;letter-spacing:.5px}
.menu a{color:var(--ink);text-decoration:none;margin-left:52px}
.menu .signup{background:#444;color:#fff;padding:10px 18px;border-radius:2px;margin-left:30px}

/* hero */
.hero{height:498px;position:relative;text-align:center;color:#fff}
.hero-photo{position:absolute;inset:0;background:linear-gradient(180deg,#3b3b3d 0%,#555 35%,#4a4a4c 70%,#2e2e30 100%)}
.hero-text{position:relative;padding-top:290px}
.hero h1{font-family:"Oswald",sans-serif;font-weight:300;font-size:54px;letter-spacing:1px}
.hero .sub{font-size:19px;font-weight:300;letter-spacing:1px;margin-top:14px}
.dots{position:absolute;left:0;right:0;top:466px;display:flex;justify-content:center;gap:8px}
.dots span{width:14px;height:14px;border-radius:50%;border:2px solid #fff}
.dots span.on{background:var(--blue)}

/* features */
.features{height:585px;position:relative}
.model{position:absolute;left:476px;top:24px;width:204px;height:561px;background:linear-gradient(180deg,#e9d6cf 0%,#e6c3bd 45%,#8b7f7c 80%,#cfc6c2 100%);border-radius:90px 90px 10px 10px}
.callout{position:absolute;font-size:11px;color:#777;line-height:1.55}
.callout h3{font-family:"Roboto",sans-serif;font-weight:500;font-size:14px;color:var(--ink);letter-spacing:.5px;margin-bottom:12px}
.callout.right{text-align:right}
.feat-svg{position:absolute;inset:0}

/* score */
.score{height:568px;background:linear-gradient(135deg,#3f98de,#3587cd);color:#fff;text-align:center;padding-top:38px}
.score .kicker{font-family:"Oswald",sans-serif;font-weight:300;font-size:27px}
.score h2{font-family:"Oswald",sans-serif;font-weight:500;font-size:31px;margin-top:4px}
.score .sub{font-size:13px;margin-top:14px;letter-spacing:.3px}
.board{width:586px;margin:26px auto 0;background:#fff;color:var(--ink);text-align:left;border-collapse:collapse;font-size:12px}
.board th{background:var(--table-head);color:#fff;height:42px;font-weight:500;font-size:14px;text-align:left;padding:0 12px}
.board td{height:43px;border-bottom:1px solid var(--line);padding:0 12px;font-weight:500;font-size:12px}
.board .sno{width:56px}
.board .today{width:160px}
.pt{display:inline-block;width:32px;height:25px;line-height:25px;text-align:center;color:#fff;font-weight:500;margin-right:4px}
.pt.up{background:var(--blue)}
.pt.down{background:var(--score-neg)}
.net{margin-left:8px}

/* prizes */
.prizes{height:798px;padding-top:52px}
.center-head{text-align:center}
.center-head h2{font-family:"Oswald",sans-serif;font-weight:400;font-size:24px}
.center-head p{width:760px;margin:12px auto 0;text-align:center}
.rule{height:1px;background:var(--line);margin:26px 0}
.group-title{font-family:"Oswald",sans-serif;font-weight:400;font-size:19px;margin-bottom:14px}
.prize-grid{display:grid;grid-template-columns:repeat(4,1fr);gap:16px}
.prize-img{height:150px;border:1px solid var(--line);background:linear-gradient(180deg,#f7f7f7,#ececec)}
.prize h4{font-weight:500;font-size:13px;margin-top:20px}
.prize p{font-size:11.5px;line-height:1.6;margin-top:8px}
.other{margin-top:40px}

/* know */
.know{height:454px;position:relative;color:#fff;padding-top:46px}
.know-photo{position:absolute;inset:0;background:linear-gradient(135deg,#343434,#262626 60%,#303030)}
.know .wrap{z-index:1}
.know .center-head p{color:#ddd}
.know-grid{display:grid;grid-template-columns:1fr 1fr;column-gap:60px;row-gap:42px;margin-top:58px}
.know h3{font-family:"Oswald",sans-serif;font-weight:400;font-size:17px;color:var(--blue)}
.know p{color:#ccc;margin-top:14px}

/* tell */
.tell{height:226px;background:var(--blue);color:#fff;text-align:center;padding-top:50px}
.tell h2{font-family:"Oswald",sans-serif;font-weight:400;font-size:24px}
.tell p{color:#fff;width:760px;margin:8px auto 0}
.btn-line{display:inline-block;margin-top:26px;border:1.5px solid #fff;color:#fff;font-size:12px;font-weight:500;width:175px;height:36px;line-height:33px;text-decoration:none}

/* legal */
.legal{height:631px;background:#f9f9f9;padding-top:44px}
.legal .kicker{font-family:"Oswald",sans-serif;font-weight:300;font-size:24px;text-align:center}
.legal h2{font-family:"Oswald",sans-serif;font-weight:400;font-size:34px;text-align:center;margin-top:0}
.legal .center-head p{margin-top:8px}
.legal .rule{margin:22px 0 26px}
.legal-cols{display:grid;grid-template-columns:1fr 1fr;column-gap:50px}
.legal h3{font-family:"Oswald",sans-serif;font-weight:400;font-size:18px;margin-bottom:8px}
.legal .item{margin-bottom:26px}
.legal p{font-size:11.5px;line-height:1.7}
.btn-solid{display:block;width:175px;height:38px;line-height:38px;margin:4px auto 0;background:var(--blue);color:#fff;text-align:center;font-size:12px;font-weight:500;text-decoration:none;border-radius:2px}

/* footer */
.footer{height:240px;background:var(--footer);color:#fff;text-align:center;padding-top:30px}
.social{display:flex;justify-content:center;gap:18px}
.social span{width:58px;height:58px;border-radius:50%;border:1.5px solid #bbb;display:flex;align-items:center;justify-content:center}
.social span i{width:6px;height:6px;border-radius:50%;background:#ddd}
.footer-rule{height:1px;background:#3d3d3d;margin:26px 87px 0}
.footer-links{margin-top:24px;font-size:12px;letter-spacing:.5px}
.footer-links a{color:#eee;text-decoration:none;margin:0 34px}
.footer-links i{font-style:normal;color:#777}
.copy{font-size:11px;color:#bbb;margin-top:18px}
</style>
</head>
<body>

<header class="topbar">
  <div class="brand"><span class="brand-mark"></span>VENDROW</div>
  <nav class="menu">
    <a href="#">BLOG</a>
    <a href="#">FORUM</a>
    <a href="#">CONTACT</a>
    <a href="#" class="signup">SIGN UP</a>
  </nav>
</header>

<section class="hero">
  <div class="hero-photo" role="img" aria-label="Three models in dresses posing in a studio"></div>
  <div class="hero-text">
    <h1>FASHION CONTEST</h1>
    <div class="sub">CALLING ALL FASHION STUDENTS, DESIGNERS, STYLISTS, MERCHANDISERS</div>
  </div>
  <div class="dots"><span></span><span class="on"></span><span></span></div>
</section>

<section class="features">
  <div class="model" role="img" aria-label="Model in a pink blouse and grey mini skirt"></div>
  <svg class="feat-svg" width="1200" height="585" viewBox="0 0 1200 585">
    <g fill="none" stroke="#d5d5d5" stroke-width="1.5">
      <polyline points="140,255 120,318 140,381"/>
      <polyline points="1060,255 1080,318 1060,381"/>
    </g>
    <g fill="none" stroke="#bbb" stroke-width="1">
      <polyline points="330,165 470,165 520,205"/>
      <polyline points="330,295 470,295 540,320"/>
      <polyline points="330,475 470,475 520,450"/>
      <polyline points="860,175 720,175 660,230"/>
      <polyline points="860,345 720,345 660,360"/>
      <polyline points="860,470 720,470 640,470"/>
    </g>
    <g font-family="Roboto, sans-serif" font-size="11" font-weight="700" fill="#fff" text-anchor="middle">
      <polygon points="283,211 298,220 298,238 283,247 268,238 268,220" fill="#d8327a"/><text x="283" y="233">01</text>
      <polygon points="283,354 298,363 298,381 283,390 268,381 268,363" fill="#23a59b"/><text x="283" y="376">02</text>
      <polygon points="283,512 298,521 298,539 283,548 268,539 268,521" fill="#f0652c"/><text x="283" y="534">03</text>
      <polygon points="917,227 932,236 932,254 917,263 902,254 902,236" fill="#4a3a94"/><text x="917" y="249">04</text>
      <polygon points="884,400 899,409 899,427 884,436 869,427 869,409" fill="#ef4a3c"/><text x="884" y="422">05</text>
      <polygon points="884,525 899,534 899,552 884,561 869,552 869,534" fill="#b0559a"/><text x="884" y="547">06</text>
    </g>
  </svg>
  <div class="callout" style="left:337px;top:140px"><h3>NECKLINES</h3>Asymmetric<br>Banded<br>Cowl</div>
  <div class="callout" style="left:337px;top:270px"><h3>PRINTS</h3>Leopard Dress<br>Snake Dress<br>Alligator Dress</div>
  <div class="callout" style="left:337px;top:450px"><h3>LENGTHS</h3>Boy Short<br>Regular Short<br>Bermuda</div>
  <div class="callout right" style="right:338px;top:163px"><h3>MATERIALS</h3>Batiste<br>Lace<br>Eyelet</div>
  <div class="callout right" style="right:338px;top:333px"><h3>WAISTLINES</h3>Empire<br>High-waist<br>Waist &amp; Hipbone</div>
  <div class="callout right" style="right:338px;top:458px"><h3>LENGTHS</h3>Pedal Pusher<br>Ankle<br>Full-Lengths</div>
</section>

<section class="score">
  <div class="kicker">SCORE POINTS</div>
  <h2>AND SEE WHERE YOU STAND</h2>
  <div class="sub">EARN POINTS FOR EACH IMAGE, BUT WATCH OUT! MISTAKES &amp; UNJUSTIFIED SKIPS WILL COST YOU POINTS</div>
  <table class="board">
    <thead><tr><th class="sno">S.NO</th><th>NAME</th><th class="today">TODAY</th></tr></thead>
    <tbody>
      <tr><td>01</td><td>DANA MORREL</td><td><span class="pt up">10</span><span class="pt down">-11</span><span class="net">-6</span></td></tr>
      <tr><td>02</td><td>SED UT PERSPICIATIS UNDE</td><td><span class="pt up">09</span><span class="pt down">-06</span><span class="net">-5</span></td></tr>
      <tr><td>03</td><td>NATUS ERROR SIT VOLUPTATEM</td><td><span class="pt up">07</span><span class="pt down">-05</span><span class="net">-2</span></td></tr>
      <tr><td>04</td><td>ACCUSANTIUM DOLOREMQUE</td><td><span class="pt up">03</span><span class="pt down">-13</span><span class="net">-1</span></td></tr>
      <tr><td>05</td><td>QUAERAT VOLUPTATEM</td><td><span class="pt up">02</span><span class="pt down">-04</span><span class="net">-7</span></td></tr>
      <tr><td>06</td><td>INVENTORE VERITATIS ET QUASI</td><td><span class="pt up">01</span><span class="pt down">-09</span><span class="net">-6</span></td></tr>
      <tr><td>07</td><td>CONSEQUUNTUR MAGNI</td><td><span class="pt up">10</span><span class="pt down">-12</span><span class="net">-2</span></td></tr>
    </tbody>
  </table>
</section>

<section class="prizes">
  <div class="wrap">
    <div class="center-head">
      <h2>WIN AWESOME PRIZES</h2>
      <p>Sed ut perspiciatis unde omnis iste natus error sit voluptatem accusantium doloremque laudantium, totam rem aperiam, eaque ipsa quae ab illo inventore veritatis et quasi architecto beatae vitae dicta sunt explicabo.</p>
    </div>
    <div class="rule"></div>
    <div class="group-title">GRAND PRIZES</div>
    <div class="prize-grid">
      <div class="prize"><div class="prize-img" role="img" aria-label="Tablet with stylus"></div><h4>TABLO MAX</h4><p>Sed ut perspiciatis unde omnis iste natus err beatae vitae dicta sunt explicabo.</p></div>
      <div class="prize"><div class="prize-img" role="img" aria-label="Compact digital camera"></div><h4>KELVAR SNAPLINE</h4><p>Sed ut perspiciatis unde omnis iste natus err beatae vitae dicta sunt explicabo.</p></div>
      <div class="prize"><div class="prize-img" role="img" aria-label="Small Wi-Fi digital camera"></div><h4>WI-FI DIGITAL CAMERA</h4><p>Sed ut perspiciatis unde omnis iste natus err beatae vitae dicta sunt explicabo.</p></div>
      <div class="prize"><div class="prize-img" role="img" aria-label="White sewing machine"></div><h4>QM480TXV SEWING MACHINE</h4><p>Sed ut perspiciatis unde omnis iste natus err beatae vitae dicta sunt explicabo.</p></div>
    </div>
    <div class="group-title other">OTHER PRIZES</div>
    <div class="prize-grid">
      <div class="prize"><div class="prize-img" role="img" aria-label="Wireless earbuds in a charging case"></div><h4>NORAL EARLETS</h4><p>Sed ut perspiciatis unde omnis iste natus err beatae vitae dicta sunt explicabo.</p></div>
      <div class="prize"><div class="prize-img" role="img" aria-label="Shopping bag gift card"></div><h4>KETO</h4><p>Sed ut perspiciatis unde omnis iste natus err beatae vitae dicta sunt explicabo.</p></div>
      <div class="prize"><div class="prize-img" role="img" aria-label="Store gift card"></div><h4>VIMO</h4><p>Sed ut perspiciatis unde omnis iste natus err beatae vitae dicta sunt explicabo.</p></div>
      <div class="prize"><div class="prize-img" role="img" aria-label="Cosmetics store gift card"></div><h4>LUMIREL</h4><p>Sed ut perspiciatis unde omnis iste natus err beatae vitae dicta sunt explicabo.</p></div>
    </div>
  </div>
</section>

<section class="know">
  <div class="know-photo" role="img" aria-label="Dark fashion photo backdrop"></div>
  <div class="wrap">
    <div class="center-head">
      <h2>WHAT YOU NEED TO KNOW</h2>
      <p>Sed ut perspiciatis unde omnis iste natus error sit voluptatem accusantium doloremque laudantium, totam rem aperiam, eaque ipsa quae ab illo inventore veritatis et quasi architecto beatae vitae dicta sunt explicabo.</p>
    </div>
    <div class="know-grid">
      <div><h3>HOW TO ENTER</h3><p>Sed ut perspiciatis unde omnis iste natus error sit voluptatem accusantium doloremque laudantium, totam rem aperiam, eaque ipsa quae ab illo inventore veritatis et quasi architecto beatae vitae dicta sunt explicabo.</p></div>
      <div><h3>WHAT ARE THE CONTEST DATES</h3><p>Sed ut perspiciatis unde omnis iste natus error sit voluptatem accusantium doloremque laudantium, totam rem aperiam, eaque ipsa quae ab illo inventore veritatis et quasi architecto beatae vitae dicta sunt explicabo.</p></div>
      <div><h3>HOW DO I QUALIFY?</h3><p>Sed ut perspiciatis unde omnis iste natus error sit voluptatem accusantium doloremque laudantium, totam rem aperiam, eaque ipsa quae ab illo inventore veritatis et quasi architecto beatae vitae dicta sunt explicabo.</p></div>
      <div><h3>WHAT IS THIS FOR?</h3><p>Sed ut perspiciatis unde omnis iste natus error sit voluptatem accusantium doloremque laudantium, totam rem aperiam, eaque ipsa quae ab illo inventore veritatis et quasi architecto beatae vitae dicta sunt explicabo.</p></div>
    </div>
  </div>
</section>

<section class="tell">
  <h2>TELL YOUR FRIENDS</h2>
  <p>Sed ut perspiciatis unde omnis iste natus error sit voluptatem accusantium doloremque laudantium, totam rem aperiam, eaque ipsa quae ab illo inventore veritatis et quasi architecto beatae vitae dicta sunt explicabo.</p>
  <a href="#" class="btn-line">REFERRAL FRIEND</a>
</section>

<section class="legal">
  <div class="wrap">
    <div class="kicker">THE LEGAL STUFF</div>
    <h2>TERMS &amp; CONDITIONS</h2>
    <div class="center-head"><p>Sed ut perspiciatis unde omnis iste natus error sit voluptatem accusantium doloremque laudantium, totam rem aperiam, eaque ipsa quae ab illo inventore veritatis et quasi architecto beatae vitae dicta sunt explicabo.</p></div>
    <div class="rule"></div>
    <div class="legal-cols">
      <div>
        <div class="item"><h3>ELIGIBILITY</h3><p>Sed ut perspiciatis unde omnis iste natus error sit voluptatem accusantium doloremque laudantium, totam rem hitecto beatae vitae dicta sunt explicabo.</p></div>
        <div class="item"><h3>WINNERS AND PRIZES</h3><p>Sed ut perspiciatis unde omnis iste natus error sit voluptatem accusantium doloremque laudantium, totam rem hitecto beatae vitae dicta sunt explicabo.</p></div>
        <div class="item"><h3>PRIVACY POLICY</h3><p>Sed ut perspiciatis unde omnis iste natus error sit voluptatem accusantium doloremque laudantium, totam rem hitecto beatae vitae dicta sunt explicabo.</p></div>
      </div>
      <div>
        <div class="item"><h3>JUDGING</h3><p>Sed ut perspiciatis unde omnis iste natus error sit voluptatem accusantium doloremque laudantium, totam rem aperiam, eaque ipsa quae ab illo inventore veritatis et quasi arc hitecto beatae vitae dicta sunt explicabo.</p></div>
        <div class="item"><h3>DISCLAIMER</h3><p>Sed ut perspiciatis unde omnis iste natus error sit voluptatem accusantium dolorem laudantium, totam rem aperiam, eaque ipsa quae ab illo inventore veritatis et quasi arc hitecto beatae vitae dicta sunt explicabo. Sed ut perspiciatis unde omnis iste nat us error sit voluptatem accusantium doloremque laudantium, totam rem aperiam, eaq hitecto beatae vitae dicta sunt explicabo.</p></div>
      </div>
    </div>
    <a href="#" class="btn-solid">READ MORE INFO</a>
  </div>
</section>

<footer class="footer">
  <div class="social">
    <span><i></i></span><span><i></i></span><span><i></i></span><span><i></i></span><span><i></i></span>
    <span><svg width="20" height="14" viewBox="0 0 20 14" fill="none" stroke="#ddd" stroke-width="1.5"><rect x="1" y="1" width="18" height="12"/><polyline points="1,1 10,8 19,1"/></svg></span>
  </div>
  <div class="footer-rule"></div>
  <div class="footer-links"><a href="#">HOME</a><i>|</i><a href="#">BLOG</a><i>|</i><a href="#">FORUM</a><i>|</i><a href="#">CONTACT</a></div>
  <div class="copy">© Copyrights 2017 Vendrow All Rights Reserved.</div>
</footer>

</body>
</html>
```